LOS PINARES DE ORO - EXCLUSIVE AND LUXURY REAL ESTATE PROJECT

Se trata del diseño de un mono poste grande (4 m x 2 m) o (8m x 3m) anunciando la construcción de 30 villas de lujo en un terreno en primera línea de playa en el sur de España (Cádiz).

La idea es crear expectación y transmitir lujo y exclusividad.

Target Market(s)

Clientes de alto poder adquisitivo que quieran adquirir su segunda vivienda en un entorno privilegiado a escasos pasos de una de las playas más bonitas de Cádiz.

Industry/Entity Type

REAL ESTATE

Colors

Designer to choose colors to be used in the design.

Requirements
Must have
• LOS PINARES DE ORO as the name of the development
Nice to have
• Crear expectación con ideas del tipo: “Coming soon” o “No te lo puedes perder”

```html
<!DOCTYPE html>
<html lang="en">
<head>
<meta charset="utf-8">
<title>Los Pinares de Oro – Coming Soon Billboard</title>
<link rel="stylesheet" href="https://fonts.googleapis.com/css2?family=Bebas+Neue&family=Poppins:wght@700&family=Saira+Condensed:ital,wght@0,800;1,800&display=swap">
<style>
  :root {
    --page-bg: #ffffff;
    --navy: #0a2d57;
    --mid-blue: #2f5ea6;
    --cyan: #00d4ff;
    --cyan-deep: #0a9fd0;
    --ink: #0d1626;
    --white: #f7f8fa;
    --sky-top: #3e63b1;
    --sky-mid: #9fb8d8;
    --terrace: #e6e2da;
  }
  * { margin: 0; padding: 0; box-sizing: border-box; }
  html, body {
    width: 922px;
    height: 1200px;
    overflow: hidden;
    background: var(--page-bg);
  }
  .canvas {
    position: relative;
    width: 922px;
    height: 1200px;
  }
  .billboard {
    position: absolute;
    left: 31px;
    top: 385px;
    width: 860px;
    height: 430px;
    box-shadow: 0 4px 14px rgba(0, 0, 0, 0.18);
  }
  .billboard svg { display: block; width: 100%; height: 100%; }
  .title-top {
    font-family: "Bebas Neue", sans-serif;
    fill: var(--cyan);
  }
  .title-bottom {
    font-family: "Poppins", sans-serif;
    font-weight: 700;
    fill: var(--white);
  }
  .tag-text {
    font-family: "Saira Condensed", sans-serif;
    font-weight: 800;
    font-style: italic;
  }
  .tag-coming-text { fill: var(--ink); }
  .tag-soon-text { fill: var(--white); }
  .rule { stroke: var(--white); stroke-width: 2.5; }
</style>
</head>
<body>
<main class="canvas">
  <section class="billboard" aria-label="Los Pinares de Oro – coming soon">
    <svg viewBox="0 0 1484 742" xmlns="http://www.w3.org/2000/svg">
      <defs>
        <linearGradient id="villaTones" x1="0" y1="0" x2="0" y2="1">
          <stop offset="0" stop-color="var(--sky-top)"/>
          <stop offset="0.35" stop-color="var(--sky-mid)"/>
          <stop offset="0.55" stop-color="#d9d6cf"/>
          <stop offset="1" stop-color="var(--terrace)"/>
        </linearGradient>
      </defs>

      <rect class="villa-photo" x="0" y="0" width="900" height="742" fill="url(#villaTones)"
            role="img" aria-label="Photograph of a modern white luxury villa with glass walls, wooden panels and a sunny terrace with lounge seating"/>

      <polygon class="accent-stripe" points="585,0 630,0 880,530 800,530" fill="var(--mid-blue)" opacity="0.9"/>
      <polygon class="panel-navy" points="625,0 1484,0 1484,742 950,742 870,520" fill="var(--navy)"/>
      <polygon class="accent-cyan-deep" points="800,455 835,440 975,742 940,742" fill="var(--cyan-deep)"/>
      <polygon class="accent-cyan" points="660,742 800,455 940,742" fill="var(--cyan)"/>

      <text class="title-top" x="1425" y="205" font-size="150" text-anchor="end">LOS PINARES</text>
      <text class="title-bottom" x="1430" y="330" font-size="132" text-anchor="end" letter-spacing="-2">DE ORO</text>

      <line class="rule" x1="895" y1="440" x2="1235" y2="385"/>
      <line class="rule" x1="1110" y1="425" x2="1450" y2="370"/>

      <g class="tag-coming">
        <polygon points="1040,445 1395,400 1420,445 1380,510 1020,570" fill="var(--white)"/>
        <text class="tag-text tag-coming-text" x="1205" y="530" font-size="98" text-anchor="middle" transform="rotate(-8 1205 500)">COMING</text>
      </g>

      <g class="tag-soon">
        <polygon points="815,680 860,630 1320,570 1290,710 860,735" fill="var(--ink)"/>
        <text class="tag-text tag-soon-text" x="1075" y="712" font-size="128" text-anchor="middle" transform="rotate(-8 1075 670)">SOON</text>
      </g>

      <line class="rule" x1="1200" y1="730" x2="1390" y2="712" stroke-width="1.5" opacity="0.6"/>
    </svg>
  </section>
</main>
</body>
</html>
```